Kestrel Hitches Square Business Card Design

I would like a 2 x 2 square rounded corner business card.my business manufacture vehicle hitches and uses square tubing with rounded corners and would like to incorporate the border to look like the tubing...
4127 Larkfield Ave. Fernwood, Ohio 44990
(731) 555-0187
dale@kestrelhitches.example
www.kestrelhitches.example

Target Market(s)

automotive / vehicle hitches

Industry/Entity Type

Automotive

Contact Information for Business Card

I would like a 2 x 2 square rounded corner business card.my business manufacture vehicle hitches and uses square tubing with rounded corners and would like to incorporate the border to look like the tubing... and red, white and blue theme colors

Font styles to use
Sans Serif

Colors

Designer to choose colors to be used in the design.

Requirements
Must have
• Boarder
Nice to have
• red, white, blue theme colors
Should not have
• odd colors

```html
<!DOCTYPE html>
<html lang="en">
<head>
<meta charset="utf-8">
<title>Kestrel Hitches – Square Business Card</title>
<link href="https://fonts.googleapis.com/css2?family=Lato:wght@700;900&display=swap" rel="stylesheet">
<style>
  :root {
    --flag-red: #e02b3c;
    --flag-blue: #1f3f7b;
    --ink: #1e1e1e;
    --paper: #ffffff;
    --backdrop: #efedea;
  }
  html, body {
    margin: 0;
    padding: 0;
    width: 1200px;
    height: 618px;
    overflow: hidden;
    background: var(--backdrop);
    font-family: "Lato", Arial, sans-serif;
  }
  .canvas {
    position: relative;
    width: 1200px;
    height: 618px;
  }
  .card {
    position: absolute;
    top: 62px;
    width: 504px;
    height: 502px;
    border-radius: 38px;
    overflow: hidden;
    box-shadow: 0 6px 14px rgba(0,0,0,0.18);
  }
  .card-front {
    left: 68px;
    background: var(--paper);
    text-align: center;
  }
  .card-back {
    left: 620px;
    background: var(--flag-blue);
    text-align: center;
  }
  .holder-name {
    position: absolute;
    top: 72px;
    left: 0;
    right: 0;
    margin: 0;
    color: var(--flag-red);
    font-weight: 900;
    font-size: 37px;
    line-height: 1;
  }
  .holder-title {
    position: absolute;
    top: 120px;
    left: 0;
    right: 0;
    margin: 0;
    color: var(--flag-blue);
    font-weight: 900;
    font-size: 29px;
    line-height: 1;
  }
  .address {
    position: absolute;
    top: 212px;
    left: 0;
    right: 0;
    margin: 0;
    color: var(--ink);
    font-weight: 700;
    font-size: 24px;
    line-height: 32px;
    font-style: normal;
  }
  .contact-list {
    position: absolute;
    top: 300px;
    left: 0;
    right: 0;
    margin: 0;
    padding: 0;
    list-style: none;
    color: var(--ink);
    font-weight: 700;
    font-size: 23px;
    line-height: 34px;
  }
  .contact-label {
    color: var(--flag-red);
    font-weight: 900;
  }
  .tubing-band {
    position: absolute;
    left: 0;
    bottom: 0;
    width: 504px;
    height: 80px;
    display: block;
  }
  .brand-name {
    position: absolute;
    top: 190px;
    left: 0;
    right: 0;
    margin: 0;
    color: var(--paper);
    font-weight: 700;
    font-size: 86px;
    line-height: 82px;
  }
  .brand-web {
    position: absolute;
    top: 428px;
    left: 0;
    right: 0;
    margin: 0;
    color: var(--paper);
    font-weight: 700;
    font-size: 22px;
  }
</style>
</head>
<body>
<main class="canvas">
  <section class="card card-front" aria-label="Card front">
    <h1 class="holder-name">Dale R. Whitford</h1>
    <p class="holder-title">Owner</p>
    <address class="address">4127 Larkfield Ave.<br>Fernwood, Ohio 44990</address>
    <ul class="contact-list">
      <li><span class="contact-label">P:</span> (731) 555-0187</li>
      <li><span class="contact-label">E:</span> dale@kestrelhitches.example</li>
      <li><span class="contact-label">W:</span> www.kestrelhitches.example</li>
    </ul>
    <svg class="tubing-band" viewBox="0 0 504 80" aria-hidden="true">
      <polygon points="0,34 252,13 504,34 504,80 0,80" fill="var(--flag-red)"/>
      <polygon points="0,40 252,18 504,40 504,80 0,80" fill="var(--paper)"/>
      <polygon points="0,45 252,23 504,45 504,80 0,80" fill="var(--flag-blue)"/>
    </svg>
  </section>

  <section class="card card-back" aria-label="Card back">
    <p class="brand-name">Kestrel<br>Hitches</p>
    <p class="brand-web">www.kestrelhitches.example</p>
  </section>
</main>
</body>
</html>
```